Travel Business Card

Hello. I am an award-winning travel advisor in Sydney, Australia seeking new business cards reflecting a unique style. Words to describe the design I'm seeking - Contemporary, Artsy, Vibrant, Soulful, Journey.

I loved this'Absolut' design and have created a few concepts to guide you for the back of the bus card. Feel free to use your own imagination...
maybe use elements of a Venetian mask or City (Icon), Cruise Ship, Sunshine, Beach/ Beach Hut, Buddha (Spiritual), Lotus or Palm Tree (Nature), Magic Carpet (Middle East), Whale or Waves, or enhance the pencil sketch I did...

Remember. The design should look high-end and fashionable.

Looking forward to hearing from you.
My email is miriam@plenvoritrips.example.

Many thanks.

```html
<!DOCTYPE html>
<html lang="en">
<head>
<meta charset="utf-8">
<title>Plenvori Trips – Business Card</title>
<link rel="stylesheet" href="https://fonts.googleapis.com/css2?family=Questrial&family=Nunito:wght@900&display=swap">
<style>
  :root {
    --page: #ffffff;
    --card: #ffffff;
    --card-edge: #9a9a9a;
    --ink: #1c1c1c;
    --band-red: #c8162b;
    --band-orange: #f08a1c;
    --band-yellow: #f7c51e;
    --band-green: #4fae32;
    --sky-top: #2f86d6;
    --sky-mid: #8cc7ee;
    --sea: #1f74b8;
    --collage-warm: #c9a98a;
    --logo-ink: #c8162b;
  }
  * { box-sizing: border-box; margin: 0; padding: 0; }
  html, body { width: 1200px; height: 846px; overflow: hidden; background: var(--page); }
  .canvas { position: relative; width: 1200px; height: 846px; }

  .card {
    position: absolute;
    top: 113px;
    width: 435px;
    height: 652px;
    background: var(--card);
    border: 1px solid var(--card-edge);
    overflow: hidden;
  }
  .card--front { left: 148px; }
  .card--back { left: 633px; }

  .front__waves { position: absolute; left: 0; top: 0; width: 435px; height: 200px; }

  .front__name {
    position: absolute;
    top: 152px; left: 0; width: 100%;
    text-align: center;
    font-family: "Questrial", sans-serif;
    font-size: 31px;
    letter-spacing: 0.5px;
    color: var(--ink);
  }
  .front__rule {
    position: absolute;
    top: 203px; left: 70px;
    width: 306px; height: 2px;
    background: var(--ink);
  }
  .front__phone {
    position: absolute;
    top: 222px; left: 0; width: 100%;
    text-align: center;
    font-family: "Questrial", sans-serif;
    font-size: 30px;
    color: var(--ink);
  }
  .front__email {
    position: absolute;
    bottom: 14px; left: 0; width: 100%;
    text-align: center;
    font-family: "Questrial", sans-serif;
    font-size: 18.5px;
    letter-spacing: 0.4px;
    color: var(--ink);
  }

  .back__collage {
    position: absolute; inset: 0;
    background:
      linear-gradient(180deg, var(--sky-top) 0%, var(--sky-mid) 22%, var(--sea) 38%, #e9eef2 55%, var(--collage-warm) 80%, #8e857c 100%);
  }
  .back__bands { position: absolute; left: 0; top: 420px; width: 435px; height: 110px; }
  .back__logo {
    position: absolute;
    top: 330px; left: 0; width: 100%;
    text-align: center;
    font-family: "Nunito", sans-serif;
    font-weight: 900;
    font-size: 52px;
    line-height: 1;
    color: var(--logo-ink);
  }
</style>
</head>
<body>
<main class="canvas">
  <section class="card card--front" aria-label="Business card front">
    <svg class="front__waves" viewBox="0 0 435 200" aria-hidden="true">
      <path d="M0 50 C110 20 170 -10 260 0 C330 8 380 -2 435 -5 L435 20 C380 22 330 30 260 24 C170 16 110 48 0 78 Z" fill="var(--band-red)"/>
      <path d="M0 78 C110 48 170 16 260 24 C330 30 380 22 435 20 L435 42 C380 45 330 52 260 46 C170 40 110 74 0 104 Z" fill="var(--band-orange)"/>
      <path d="M0 104 C110 74 170 40 260 46 C330 52 380 45 435 42 L435 64 C380 68 330 74 260 68 C170 64 110 100 0 130 Z" fill="var(--band-yellow)"/>
      <path d="M0 130 C110 100 170 64 260 68 C330 74 380 68 435 64 L435 86 C380 92 330 98 260 92 C170 88 110 126 0 156 Z" fill="var(--band-green)"/>
    </svg>
    <h1 class="front__name">MIRIAM TANBERG</h1>
    <div class="front__rule"></div>
    <p class="front__phone">4272-6150</p>
    <p class="front__email">MIRIAM@PLENVORITRIPS.EXAMPLE.</p>
  </section>

  <section class="card card--back" aria-label="Business card back">
    <div class="back__collage" role="img" aria-label="Travel collage: palm tree, cruise yacht on blue sea, hot air balloons, red suitcase, scooter, Eiffel Tower, glass of red wine, plate of noodles and a seated Buddha statue"></div>
    <svg class="back__bands" viewBox="0 0 435 110" aria-hidden="true">
      <path d="M0 30 C120 10 260 40 435 0 L435 16 C260 56 120 26 0 46 Z" fill="var(--band-orange)"/>
      <path d="M0 46 C120 26 260 56 435 16 L435 32 C260 72 120 42 0 62 Z" fill="var(--band-yellow)"/>
      <path d="M0 62 C120 42 260 72 435 32 L435 48 C260 88 120 58 0 78 Z" fill="var(--band-green)"/>
    </svg>
    <p class="back__logo">plenvori<br>trips</p>
  </section>
</main>
</body>
</html>
```